Real Estate For Sale Sign

I need to design a for sale sign. It needs to include The following information
Logo: Attached
Name: Corinne Vasquel,
Company Name: Gilded Harbor Real Estate,
Phone Number: 503-841-2096
BRE Licence Number 04817359 (Can Be small)
Sign size 24x30

I am not sure about including my website but I would like to see options with it. www.gildedharbor-example.com
Updates

Target Market(s)

Potential Buyers or Sellers of Real Estate. Must be easy to read.

Industry/Entity Type

Real Estate

Requirements
Must have
• I want it to feel luxurious and sharp.

```html
<!DOCTYPE html>
<html lang="en">
<head>
<meta charset="utf-8">
<title>Gilded Harbor Real Estate – For Sale Sign</title>
<link rel="stylesheet" href="https://fonts.googleapis.com/css2?family=Bebas+Neue&family=Cinzel:wght@400;600&display=swap">
<style>
  :root {
    --backdrop: #2e2e2e;
    --sign-white: #ffffff;
    --navy: #0c1331;
    --cyan: #00aee2;
    --brand-blue: #1763a6;
    --strip-grey: #6e6f71;
    --text-grey: #7a7b7d;
  }
  * { margin: 0; padding: 0; box-sizing: border-box; }
  html, body {
    width: 1200px; height: 900px; overflow: hidden;
    background: var(--backdrop);
  }
  .sign {
    position: absolute; left: 50px; top: 20px;
    width: 1100px; height: 860px;
    background: var(--sign-white);
    overflow: hidden;
  }
  .brand-header { position: absolute; left: 0; top: 0; width: 100%; height: 262px; }
  .brand-mark {
    position: absolute; left: 62px; top: 36px;
    width: 196px; height: 196px;
  }
  .brand-name {
    position: absolute; left: 290px; right: 40px; top: 52px;
    text-align: center;
    font-family: "Cinzel", serif; font-weight: 600;
    color: var(--brand-blue);
    line-height: 1;
  }
  .brand-name__main { display: block; font-size: 84px; }
  .brand-name__sub { display: block; font-size: 40px; letter-spacing: 14px; margin-top: 30px; }

  .sale-band {
    position: absolute; left: 0; top: 262px; width: 100%; height: 436px;
    background: var(--navy);
    text-align: center;
  }
  .sale-headline {
    position: absolute; left: 0; right: 0; top: 12px;
    font-family: "Bebas Neue", sans-serif;
    font-size: 190px; line-height: 1;
    color: var(--sign-white);
  }
  .agent-line {
    position: absolute; left: 0; right: 0; top: 178px;
    font-family: "Cinzel", serif; font-weight: 400;
    font-size: 70px; line-height: 1;
    color: var(--sign-white);
  }
  .agent-line__call { color: var(--cyan); font-weight: 600; text-transform: lowercase; }
  .agent-phone {
    position: absolute; left: 0; right: 0; top: 256px;
    font-family: "Bebas Neue", sans-serif;
    font-size: 200px; line-height: 1;
    color: var(--cyan);
  }

  .company-line {
    position: absolute; left: 0; right: 0; top: 712px;
    text-align: center;
    font-family: "Cinzel", serif; font-weight: 400;
    font-size: 62px; line-height: 1;
    color: var(--brand-blue);
  }

  .footer-strip { position: absolute; left: 0; top: 806px; width: 1100px; height: 54px; }
  .footer-licence {
    position: absolute; left: 52px; top: 826px;
    font-family: "Cinzel", serif; font-size: 14px;
    color: #e6e6e6; letter-spacing: 0.5px;
  }
  .footer-web {
    position: absolute; right: 52px; top: 818px;
    font-family: "Cinzel", serif; font-size: 25px;
    color: var(--sign-white); letter-spacing: 1px;
  }
</style>
</head>
<body>
  <div class="sign">
    <header class="brand-header">
      <svg class="brand-mark" viewBox="0 0 196 196" aria-hidden="true">
        <circle cx="98" cy="98" r="86" fill="none" stroke="var(--cyan)" stroke-width="10"/>
      </svg>
      <div class="brand-name">
        <span class="brand-name__main">Gilded Harbor</span>
        <span class="brand-name__sub">REAL ESTATE</span>
      </div>
    </header>

    <section class="sale-band">
      <h1 class="sale-headline">HOUSE FOR SALE</h1>
      <p class="agent-line"><span class="agent-line__call">Call</span> Corinne Vasquel</p>
      <p class="agent-phone">503-841-2096</p>
    </section>

    <p class="company-line">Gilded Harbor Real Estate</p>

    <svg class="footer-strip" viewBox="0 0 1100 54" aria-hidden="true">
      <polygon points="0,0 536,0 502,54 0,54" fill="var(--strip-grey)"/>
      <polygon points="558,0 1100,0 1100,54 524,54" fill="var(--brand-blue)"/>
    </svg>
    <p class="footer-licence">BRE Licence Number 04817359</p>
    <p class="footer-web">WWW.GILDEDHARBOR-EXAMPLE.COM</p>
  </div>
</body>
</html>
```